Cargo Van Car Wrap

We have purchased a new car and are looking for a design.

2023 Torvane 3400 Cargo Van 170"

Target Market(s)

Home Improvement - Kitchen and Bath Remodeling , Home Additions, Sunroom, Deck, Patio, Porch

Industry/Entity Type

Interior Remodeling , Home Additions . Kitchen and Bath Remodeling

Font styles to use
Sans Serif

Colors

Designer to choose colors to be used in the design.

Requirements
Must have
• Kitchen and Bathroom Pictures
Nice to have
• Office address , website, phone number and promition. 4817 Brindle Ave Silver Spring MD 20847 , www.zentrokitchenandbath.com - 3015550187

```html
<!DOCTYPE html>
<html lang="en">
<head>
<meta charset="utf-8">
<title>Zentro Kitchen &amp; Bath – Van Wrap</title>
<link rel="stylesheet" href="https://fonts.googleapis.com/css2?family=Nunito:wght@700;800&family=Oswald:wght@400&display=swap">
<style>
  :root {
    --canvas: #ffffff;
    --body-white: #eef0f0;
    --purple: #6d0f78;
    --purple-deep: #4a0c52;
    --purple-light: #8a1f96;
    --ink: #141414;
    --band-black: #1c1c1c;
    --tire: #222222;
    --rim: #b9bcbf;
    --glass: #1a1a1a;
    --text-light: #f1eef2;
    --seam: #b8bcbf;
  }
  html, body {
    margin: 0;
    padding: 0;
    width: 1200px;
    height: 797px;
    overflow: hidden;
    background: var(--canvas);
  }
  .van-wrap {
    display: block;
    width: 1200px;
    height: 797px;
  }
  .brand-name {
    font-family: "Oswald", sans-serif;
    font-weight: 400;
    fill: var(--ink);
  }
  .contact-text {
    font-family: "Nunito", sans-serif;
    font-weight: 800;
  }
  .address { fill: var(--text-light); font-size: 25px; }
  .phone { fill: var(--ink); font-size: 34px; }
  .website { fill: #d9d2dc; font-size: 33px; letter-spacing: 0.5px; }
</style>
</head>
<body>
<svg class="van-wrap" viewBox="0 0 2000 1329" xmlns="http://www.w3.org/2000/svg">
  <defs>
    <clipPath id="van-body">
      <path d="M150 690 Q 250 645 360 600 L 560 385 Q 620 318 715 312 L 1760 300 Q 1840 305 1850 400 L 1862 850 Q 1860 870 1835 872 L 160 882 Q 135 880 135 850 L 138 730 Q 140 700 150 690 Z"/>
    </clipPath>
    <linearGradient id="panel-purple" x1="0" y1="0" x2="0" y2="1">
      <stop offset="0" stop-color="#3f0a46"/>
      <stop offset="1" stop-color="#7a1486"/>
    </linearGradient>
    <linearGradient id="photo-tones" x1="0" y1="0" x2="1" y2="1">
      <stop offset="0" stop-color="#d9dde2"/>
      <stop offset="0.5" stop-color="#9aa3ad"/>
      <stop offset="1" stop-color="#6d5a3a"/>
    </linearGradient>
  </defs>

  <g class="van-body" clip-path="url(#van-body)">
    <rect class="body-base" x="0" y="280" width="2000" height="620" fill="var(--body-white)"/>

    <polygon class="address-panel" points="1010,752 1225,300 1520,300 1320,725" fill="url(#panel-purple)"/>

    <polygon class="kitchen-photo" role="img" aria-label="Photo of a remodeled kitchen with dining table, yellow chairs and pendant lights" points="1320,725 1520,300 1870,300 1870,630" fill="url(#photo-tones)"/>

    <path class="swoosh-purple" d="M130 700 Q 600 770 1100 745 Q 1500 720 1870 640 L 1870 760 L 130 760 Z" fill="var(--purple)"/>
    <path class="swoosh-black" d="M130 680 Q 600 755 1100 735 Q 1500 715 1870 625 L 1870 650 Q 1500 735 1100 752 Q 600 770 130 705 Z" fill="var(--band-black)"/>
    <rect class="band-black" x="130" y="755" width="1750" height="60" fill="var(--band-black)"/>
    <rect class="band-purple" x="450" y="815" width="1420" height="70" fill="var(--purple)"/>
    <rect class="front-bumper" x="130" y="720" width="320" height="170" fill="var(--band-black)"/>
    <path class="front-accent" d="M190 705 Q 330 735 450 750 L 450 770 Q 320 760 200 735 Z" fill="var(--purple-light)"/>
  </g>

  <path class="window" d="M370 628 L 540 440 Q 560 425 600 425 L 672 425 Q 682 428 680 440 L 675 570 Q 660 585 600 600 Z" fill="var(--glass)"/>
  <path class="side-mirror" d="M410 545 L 440 540 L 445 610 L 415 612 Z" fill="var(--ink)"/>
  <rect class="door-handle" x="605" y="636" width="65" height="12" rx="6" fill="var(--band-black)"/>

  <g class="panel-seams" stroke="var(--seam)" stroke-width="2" fill="none">
    <path d="M710 312 L 710 880"/>
    <path d="M1100 305 L 1105 880"/>
    <path d="M410 630 L 410 880"/>
    <rect x="740" y="418" width="360" height="195" rx="30"/>
  </g>

  <g class="headlight">
    <path d="M160 680 L 245 672 L 235 705 L 160 718 Z" fill="#c9cdd0"/>
  </g>
  <path class="tail-light" d="M1815 600 L 1855 600 L 1858 745 L 1818 745 Z" fill="#c62828"/>

  <g class="brand">
    <text class="brand-name" x="900" y="537" text-anchor="middle" font-size="96" letter-spacing="6">ZENTRO</text>
    <text class="brand-name" x="900" y="590" text-anchor="middle" font-size="34" letter-spacing="5">KITCHEN &amp; BATH</text>
  </g>

  <g class="address-block">
    <line x1="1160" y1="462" x2="1398" y2="462" stroke="var(--text-light)" stroke-width="2"/>
    <text class="contact-text address" x="1170" y="496">4817 Brindle Ave</text>
    <text class="contact-text address" x="1170" y="527">Silver Spring</text>
    <text class="contact-text address" x="1170" y="557">MD 20847</text>
    <line x1="1112" y1="577" x2="1350" y2="577" stroke="var(--text-light)" stroke-width="2"/>
  </g>

  <g class="phone-block">
    <rect x="417" y="667" width="34" height="34" rx="6" fill="var(--purple)"/>
    <path d="M426 676 Q 428 673 431 675 L 435 680 Q 436 683 433 685 Q 435 690 440 693 Q 442 690 445 691 L 449 695 Q 450 698 447 700 Q 440 704 430 692 Q 422 682 426 676 Z" fill="#ffffff"/>
    <text class="contact-text phone" x="458" y="696">3015550187</text>
  </g>

  <text class="contact-text website" x="907" y="852" text-anchor="middle">www.zentrokitchenandbath.com</text>

  <g class="wheels">
    <circle cx="345" cy="885" r="100" fill="var(--tire)"/>
    <circle cx="345" cy="885" r="57" fill="var(--rim)"/>
    <circle cx="345" cy="885" r="20" fill="#555"/>
    <circle cx="1465" cy="885" r="100" fill="var(--tire)"/>
    <circle cx="1465" cy="885" r="57" fill="var(--rim)"/>
    <circle cx="1465" cy="885" r="20" fill="#555"/>
  </g>
</svg>
</body>
</html>
```